Auto Mechanic business card

Need a general business card for GearFixer.
Name on card should be 'Roadside Wrench'
Tel # (869) 412 3097
Address is - Palm Lane, Basseterre, St. Kitts
Whatsapp and facebook symbols should be added
On back of card should include services offered
General Repairs
Brakes
Tune Ups
Suspensions
Oil Leaks
Dent repairs
Suspensions
Car Sales
Tyre Repairs
General service
Check Engine Light
Minor Electricals

Target Market(s)

General Population, University students

Industry/Entity Type

Auto Mechanic

Contact Information for Business Card

Roadside Wrench

Requirements
Must have
• 2 Sides

```html
<!DOCTYPE html>
<html lang="en">
<head>
<meta charset="utf-8">
<title>Roadside Wrench – Business Card</title>
<link href="https://fonts.googleapis.com/css2?family=Arimo:wght@400;700&display=swap" rel="stylesheet">
<style>
  :root {
    --backdrop: #b0b0b0;
    --card: #ffffff;
    --brand-red: #d50e29;
    --ink: #1e1e1e;
    --slate: #263238;
    --white: #ffffff;
  }
  * { margin: 0; padding: 0; box-sizing: border-box; }
  html, body { width: 1134px; height: 1200px; overflow: hidden; }
  body {
    background: var(--backdrop);
    font-family: "Arimo", Arial, sans-serif;
    position: relative;
  }
  .card {
    position: absolute;
    left: 275px;
    width: 584px;
    height: 351px;
    background: var(--card);
    overflow: hidden;
  }
  .card--front { top: 208px; }
  .card--back { top: 641px; }
  .card__shapes { position: absolute; inset: 0; }
  .card__shapes .red { fill: var(--brand-red); }

  .brand-name {
    position: absolute;
    font-weight: 700;
    color: var(--ink);
    line-height: 1;
    letter-spacing: -0.5px;
  }
  .card--front .brand-name { left: 92px; top: 124px; font-size: 42px; line-height: 40px; }
  .card--back .brand-name { left: 385px; top: 58px; font-size: 18px; line-height: 17px; }

  .contact { position: absolute; left: 44px; top: 231px; color: var(--white); }
  .contact__phone { font-weight: 700; font-size: 22px; line-height: 26px; letter-spacing: 0.2px; }
  .contact__address { font-size: 20px; line-height: 28px; letter-spacing: 0.9px; }

  .social { position: absolute; top: 251px; left: 482px; display: flex; gap: 5px; }
  .social__dot { width: 34px; height: 34px; border-radius: 50%; background: var(--white); }

  .services-title {
    position: absolute; left: 44px; top: 88px;
    font-size: 36px; line-height: 40px; letter-spacing: 0.4px;
  }
  .services-title__light { color: var(--brand-red); font-weight: 400; }
  .services-title__bold { color: var(--slate); font-weight: 700; }

  .services-list {
    position: absolute; left: 44px; top: 157px;
    list-style: none; font-size: 19px; line-height: 24px;
    letter-spacing: 0.55px; color: var(--ink);
  }
  .services-list .sep { color: var(--brand-red); padding: 0 10px; }
</style>
</head>
<body>

<section class="card card--front" aria-label="Front of business card">
  <svg class="card__shapes" width="584" height="351" viewBox="0 0 584 351" aria-hidden="true">
    <polygon class="red" points="0,212 505,212 417,300 0,300"/>
    <polygon class="red" points="584,147 584,300 425,300"/>
    <polygon class="red" points="411,300 423,300 374,351 362,351"/>
  </svg>
  <div class="brand-name">Roadside<br>Wrench</div>
  <div class="contact">
    <p class="contact__phone">Tel # (869) 412 3097</p>
    <p class="contact__address">Palm Lane, Basseterre, St. Kitts</p>
  </div>
  <div class="social" aria-label="Social profiles">
    <span class="social__dot" aria-label="Social profile"></span>
    <span class="social__dot" aria-label="Messaging contact"></span>
  </div>
</section>

<section class="card card--back" aria-label="Back of business card">
  <svg class="card__shapes" width="584" height="351" viewBox="0 0 584 351" aria-hidden="true">
    <polygon class="red" points="0,128 366,128 355,139 0,139"/>
    <polygon class="red" points="584,147 584,300 422,300"/>
    <polygon class="red" points="0,300 401,300 353,351 0,351"/>
    <polygon class="red" points="411,300 422,300 374,351 363,351"/>
  </svg>
  <div class="brand-name">Roadside<br>Wrench</div>
  <h2 class="services-title"><span class="services-title__light">CAR</span><span class="services-title__bold">SERVICES</span></h2>
  <ul class="services-list">
    <li>General Repairs<span class="sep">I</span>Brakes<span class="sep">I</span>Tune Ups</li>
    <li>Suspensions<span class="sep">I</span>Oil Leaks<span class="sep">I</span>Dent repairs</li>
    <li>Suspensions<span class="sep">I</span>Car Sales<span class="sep">I</span>Tyre Repairs</li>
    <li>General service<span class="sep">I</span>Check Engine Light</li>
    <li>Minor Electricals</li>
  </ul>
</section>

</body>
</html>
```